Flyer Design

Mobile (Dustless) Shot Blasting.Graffiti Removal, Brick and Stone restoration, Paint Stripping from garden gates to Ships.No job too big or Small.No Chemicals - just Air, Water and recycled abrasive.Fully pressure controlled to prevent damage to underlying surfaces.

Target Market(s)

Domestic and commercial

Industry/Entity Type

Paint

Requirements
Nice to have
• Before and after paint removal to bare steel.
• Before and after cleaned brick/ stone work and graffiti removal

```html
<!DOCTYPE html>
<html lang="en">
<head>
<meta charset="utf-8">
<title>Ridgeline Blasting – Mobile Shot Blasting Flyer</title>
<link href="https://fonts.googleapis.com/css2?family=Roboto+Condensed:wght@700&family=Lato:wght@400;700&family=Roboto:wght@400&display=swap" rel="stylesheet">
<style>
  :root {
    --green: #3d9a3c;
    --green-dark: #2f8030;
    --charcoal: #2e2e2e;
    --ink: #2a2a2a;
    --panel-top: #ffffff;
    --panel-bottom: #d9d9d9;
    --page: #ecebe8;
    --white: #ffffff;
  }
  * { margin: 0; padding: 0; box-sizing: border-box; }
  html, body { width: 825px; height: 1200px; overflow: hidden; }
  body { background: var(--page); position: relative; }

  .flyer {
    position: absolute; left: 88px; top: 140px;
    width: 652px; height: 920px; overflow: hidden;
    background: var(--white);
    box-shadow: 0 2px 10px rgba(0,0,0,.18);
  }
  .hero-photo {
    position: absolute; left: 0; top: 0; width: 652px; height: 480px;
    background: linear-gradient(135deg, #c9c2b6 0%, #a89a86 35%, #8a7a66 55%, #c78a4a 70%, #9aa0a2 100%);
  }
  .shapes { position: absolute; left: 0; top: 0; width: 652px; height: 920px; }

  .brand {
    position: absolute; left: 405px; top: 66px; width: 230px;
    display: flex; align-items: center; gap: 10px;
    font-family: "Lato", sans-serif; font-weight: 700; font-size: 19px;
    letter-spacing: .5px; color: var(--white); text-transform: uppercase;
  }
  .brand-dot { width: 22px; height: 22px; border-radius: 50%; background: var(--green); flex: none; }

  .service-title {
    position: absolute; left: 33px; top: 500px;
    font-family: "Roboto Condensed", sans-serif; font-weight: 700; line-height: 1;
  }
  .service-title .line-a { display: block; color: var(--white); font-size: 28px; }
  .service-title .line-b { display: block; color: var(--ink); font-size: 45px; margin-top: 4px; }

  .work-photo {
    position: absolute; left: 0; top: 610px; width: 332px; height: 136px;
    border: 3px solid var(--white); border-left: 0;
    background: linear-gradient(120deg, #5a6a80 0%, #b9c0c4 40%, #d5d8d8 70%, #9ea4a6 100%);
  }

  .services-list {
    position: absolute; left: 33px; top: 775px; width: 300px;
    font-family: "Lato", sans-serif; font-size: 16.5px; line-height: 22px; color: var(--white);
  }

  .tagline {
    position: absolute; right: 32px; top: 442px; text-align: right;
    font-family: "Roboto Condensed", sans-serif; font-weight: 700; font-size: 47px; line-height: 52px;
  }
  .tagline .dark { display: block; color: var(--ink); }
  .tagline .accent { display: block; color: var(--green); }

  .intro {
    position: absolute; right: 38px; top: 590px; width: 280px; text-align: right;
    font-family: "Roboto", sans-serif; font-size: 15px; line-height: 20px; color: var(--ink);
  }

  .promise {
    position: absolute; right: 43px; top: 695px; text-align: right;
    font-family: "Lato", sans-serif; font-weight: 700; font-size: 24px; line-height: 31px;
  }
  .promise .dark { display: block; color: var(--ink); }
  .promise .accent { display: block; color: var(--green); }

  .phone {
    position: absolute; left: 367px; top: 811px; width: 285px; height: 34px;
    background: var(--green); border-radius: 17px 0 0 17px;
    font-family: "Lato", sans-serif; font-weight: 700; font-size: 16.5px;
    color: var(--white); line-height: 34px; padding-left: 21px;
  }

  .site-footer {
    position: absolute; left: 0; top: 865px; width: 652px; height: 55px;
    background: var(--charcoal);
    font-family: "Lato", sans-serif; font-size: 19px; letter-spacing: 3.6px;
    color: var(--white); text-align: center; line-height: 55px;
  }
</style>
</head>
<body>
  <div class="flyer">
    <div class="hero-photo" role="img" aria-label="Photo of a worker in a welding mask and leather jacket cutting steel in a workshop, sparks flying"></div>

    <svg class="shapes" viewBox="0 0 652 920" aria-hidden="true">
      <defs>
        <linearGradient id="panelFill" x1="0" y1="0" x2="0" y2="1">
          <stop offset="0" stop-color="var(--panel-top)"/>
          <stop offset="1" stop-color="var(--panel-bottom)"/>
        </linearGradient>
        <linearGradient id="greenFill" x1="0" y1="0" x2="1" y2="0">
          <stop offset="0" stop-color="#358c35"/>
          <stop offset="1" stop-color="#4aa844"/>
        </linearGradient>
      </defs>
      <!-- header band -->
      <path d="M270,0 C290,110 360,168 480,176 L652,182 L652,0 Z" fill="var(--white)"/>
      <path d="M282,0 C302,102 370,160 482,168 L652,174 L652,0 Z" fill="var(--green)"/>
      <path d="M292,0 C312,96 378,152 484,160 L652,166 L652,0 Z" fill="var(--charcoal)"/>
      <!-- left green title block -->
      <path d="M0,472 C150,465 270,450 337,430 L337,606 L0,606 Z" fill="url(#greenFill)"/>
      <!-- right light panel -->
      <path d="M320,470 C330,402 372,380 440,372 L652,364 L652,382 L440,390 C382,397 347,422 338,470 Z" fill="var(--green)"/>
      <path d="M338,470 C347,422 382,397 440,390 L652,382 L652,865 L338,865 Z" fill="url(#panelFill)"/>
      <!-- bottom-left green block -->
      <rect x="0" y="749" width="338" height="116" fill="url(#greenFill)"/>
    </svg>

    <div class="brand"><span class="brand-dot"></span><span>Ridgeline Blasting</span></div>

    <h1 class="service-title">
      <span class="line-a">Mobile (Dustless)</span>
      <span class="line-b">Shot Blasting</span>
    </h1>

    <div class="work-photo" role="img" aria-label="Photo of an operator in gloves blasting a steel surface clean"></div>

    <p class="services-list">Graffiti Removal, Brick and Stone restoration, Paint Stripping from garden gates to Ships.</p>

    <h2 class="tagline">
      <span class="dark">No job too</span>
      <span class="accent">big or Small</span>
    </h2>

    <p class="intro">No Chemicals - just Air, Water and recycled abrasive. Fully pressure controlled to prevent damage to underlying surfaces.</p>

    <p class="promise">
      <span class="dark">No Chemicals</span>
      <span class="accent">Just Air, Water</span>
      <span class="dark">&amp; recycled abrasive</span>
    </p>

    <div class="phone">Tel (mobile) 0770 090 0123</div>

    <footer class="site-footer">www.ridgelineblasting.co.uk.</footer>
  </div>
</body>
</html>
```